“Bright Tide” Spring Fair Poster

We are putting together a school and community fair. We need a poster designed to advertise the event and give some important information to would be attendees. We’d like the poster graphics to evoke a minimalistic and futuristic aesthetic, be bold, yet fun! We will printing the posters, so we will need for them to be at high resolution and ready to send to print.

Target Market(s)

Students, Parents, and Community members

Industry/Entity Type

School

Font styles to use
Sans Serif

Colors
33a6d7
fabb78
9d9d9d
ffffff
1b1b1b
33b8a4

Requirements
Must have
• Bright Tide
• Birch & Lantern Spring Fair 2018
• Friday, May 18th
• 5:00-9:00pm
• Tickets Will Be Available at Select Pick up & Drop Off Times
• Come Enjoy a Futuristic Evening of Food, Music, Entertainment, & Fun!
Nice to have
• We’d love to see a bold and graphic poster with a futuristic feel!
• See the sample image below from previous event poster and additional images for mood and inspiration. Would love to see metallics (silver or metallic colors)

```html
<!DOCTYPE html>
<html lang="en">
<head>
<meta charset="utf-8">
<title>Bright Tide – Birch &amp; Lantern Spring Fair 2018</title>
<link rel="stylesheet" href="https://fonts.googleapis.com/css2?family=Audiowide&family=Orbitron:wght@900&display=swap">
<style>
  :root {
    --night: #04121a;
    --deep-teal: #0a3a4c;
    --cyan: #33a6d7;
    --cyan-glow: #5fd6f5;
    --white: #ffffff;
  }
  html, body {
    margin: 0;
    padding: 0;
    width: 849px;
    height: 1200px;
    overflow: hidden;
    background: var(--night);
  }
  .poster {
    position: relative;
    width: 849px;
    height: 1200px;
    overflow: hidden;
  }
  .poster__artwork {
    position: absolute;
    inset: 0;
    background:
      radial-gradient(circle at 436px 580px, #2ab3dc 0px, #137a9e 150px, #0b4a63 264px, #0a3a4c 300px, #072836 520px, var(--night) 820px);
  }
  .poster__type {
    position: absolute;
    inset: 0;
  }
  .info-text {
    font-family: "Audiowide", sans-serif;
    fill: var(--white);
    text-transform: uppercase;
  }
  .event-title {
    font-family: "Orbitron", sans-serif;
    font-weight: 900;
    fill: var(--white);
    filter: drop-shadow(0 0 6px var(--cyan-glow)) drop-shadow(0 0 14px var(--cyan));
  }
  .orb-ring {
    fill: none;
    stroke: var(--cyan-glow);
    stroke-width: 6;
    filter: drop-shadow(0 0 8px var(--cyan));
  }
</style>
</head>
<body>
<main class="poster">
  <div class="poster__artwork" role="img" aria-label="Glowing cyan network of connected points and lines forming a sphere on a dark teal background"></div>

  <svg class="poster__type" width="849" height="1200" viewBox="0 0 849 1200">
    <circle class="orb-ring" cx="436" cy="580" r="264"/>

    <g class="event-header">
      <text class="info-text" x="426" y="80" font-size="28" text-anchor="middle" textLength="748" lengthAdjust="spacingAndGlyphs">Birch &amp; Lantern Spring Fair 2018</text>
      <text class="info-text" x="418" y="128" font-size="28" text-anchor="middle" textLength="393" lengthAdjust="spacingAndGlyphs">Friday, May 18th</text>
      <text class="info-text" x="424" y="163" font-size="28" text-anchor="middle" textLength="280" lengthAdjust="spacingAndGlyphs">5:00-9:00pm</text>
    </g>

    <text class="event-title" x="428" y="624" font-size="120" text-anchor="middle" textLength="700" lengthAdjust="spacingAndGlyphs">BRIGHT TIDE</text>

    <g class="event-details">
      <text class="info-text" x="420" y="1006" font-size="24" text-anchor="middle" textLength="536" lengthAdjust="spacingAndGlyphs">Tickets will be available</text>
      <text class="info-text" x="426" y="1036" font-size="24" text-anchor="middle" textLength="716" lengthAdjust="spacingAndGlyphs">at select pick up &amp; drop off times</text>
      <text class="info-text" x="422" y="1096" font-size="24" text-anchor="middle" textLength="676" lengthAdjust="spacingAndGlyphs">Come enjoy a futuristic evening</text>
      <text class="info-text" x="421" y="1127" font-size="24" text-anchor="middle" textLength="758" lengthAdjust="spacingAndGlyphs">of food, music, entertainment, &amp; fun!</text>
    </g>
  </svg>
</main>
</body>
</html>
```